I am looking for help designing my new business cards. I would like rounded edges and a raised logo on the back of the card. I have 2 Logos. One with a boat in it and one without. I'd like the one on the back to be the one that includes the boat and just the name on the front. I have included multiple formats of my logo. Please let me know if you need anymore.

Target Market(s)

Potential buyers and other sales brokers

Industry/Entity Type

Sales - Yacht / Boat Sales

Contact Information for Business Card

Id liike the front to include just the business name portion of the logo along with my name (Corwin Dalby), phone number (555.318.6027), website address (www.dalbymarineco.example) and not my physical address but just "Port Lindell, SC". The back should include my full logo that has the boat included. This portion I'd prefer raised amd take up the majority of the space there. Thanks!!

Colors
0054AA
0677BA
7BADD7
CADEEF
E8F1F8
0094D4
00A9DD
6FCCEA
C7EBF8
E9F6FB

Requirements
Must have
• Double sided
Nice to have
• My email address: Corwin@dalbymarineco.example The NMTG logo somewhere small on the front of the card
Should not have
• My full address, prefer only "Port Lindell, SC"

```html
<!DOCTYPE html>
<html lang="en">
<head>
<meta charset="utf-8">
<title>Dalby Marine Co — Business Cards</title>
<link href="https://fonts.googleapis.com/css2?family=Jost:wght@400;500;700&display=swap" rel="stylesheet">
<style>
  :root{
    --navy:#1f2a6b;
    --ocean:#0677BA;
    --sky:#2a8fd0;
    --mist:#CADEEF;
    --foam:#E8F1F8;
    --paper:#ffffff;
    --backdrop:#e4e5e7;
  }
  *{margin:0;padding:0;box-sizing:border-box}
  html,body{width:1200px;height:800px;overflow:hidden}
  body{background:var(--backdrop);font-family:"Jost",sans-serif;position:relative}
  .card{position:absolute;width:540px;height:309px;background:var(--paper);border-radius:16px;overflow:hidden;box-shadow:0 10px 24px rgba(0,0,0,.12)}
  .card--back{left:40px;top:246px}
  .card--front{left:620px;top:246px}
  .card svg.wave{position:absolute;inset:0;width:100%;height:100%}
  .boat-art{position:absolute;border-radius:40% 60% 30% 50%;background:linear-gradient(135deg,var(--foam),var(--mist) 55%,var(--ocean))}
  .card--front .boat-art{left:36px;top:22px;width:240px;height:110px}
  .card--back .boat-art{left:300px;top:125px;width:210px;height:110px}
  .wordmark{position:absolute;color:var(--navy);font-weight:700;text-transform:uppercase;line-height:1;letter-spacing:.02em}
  .card--front .wordmark{right:30px;top:48px;text-align:right}
  .card--back .wordmark{left:30px;top:40px}
  .wordmark .big{display:block;font-size:52px}
  .wordmark .small{display:block;font-size:20px;letter-spacing:.18em;margin-top:4px}
  .contact{position:absolute;left:28px;top:212px;color:var(--paper);font-weight:400}
  .contact .name{font-size:15px;margin-bottom:8px}
  .contact .name strong{font-weight:500;text-transform:uppercase;letter-spacing:.03em}
  .contact .line{font-size:13px;display:flex;align-items:center;gap:6px;white-space:nowrap}
  .contact .line svg{width:12px;height:12px;fill:var(--paper)}
  .contact .rule{margin-top:10px;width:440px;height:1px;background:rgba(255,255,255,.7)}
  .badge{position:absolute;right:24px;top:214px;width:22px;height:22px;border-radius:50%;background:var(--paper);opacity:.85}
  .website{position:absolute;left:40px;bottom:26px;color:var(--paper);font-size:16px;letter-spacing:.22em}
</style>
</head>
<body>

<section class="card card--back" aria-label="Card back">
  <svg class="wave" viewBox="0 0 540 309" preserveAspectRatio="none" aria-hidden="true">
    <path d="M0,150 C90,140 170,190 250,200 C320,210 350,160 420,190 C480,215 510,250 540,245 L540,309 L0,309Z" fill="var(--sky)"/>
    <path d="M0,140 C90,128 170,178 250,188 C320,198 350,148 420,178" fill="none" stroke="var(--sky)" stroke-width="3"/>
  </svg>
  <div class="wordmark"><span class="big">Dalby</span><span class="small">Marine Co</span></div>
  <div class="boat-art" role="img" aria-label="Line illustration of a centre-console boat cutting through waves"></div>
  <div class="website">www.dalbymarineco.example</div>
</section>

<section class="card card--front" aria-label="Card front">
  <svg class="wave" viewBox="0 0 540 309" preserveAspectRatio="none" aria-hidden="true">
    <path d="M0,90 C90,80 160,120 250,150 C340,180 380,150 440,175 C490,195 510,200 540,195 L540,309 L0,309Z" fill="var(--sky)"/>
    <path d="M0,80 C90,70 160,110 250,140 C340,170 380,140 440,165 C490,185 510,190 540,185" fill="none" stroke="var(--sky)" stroke-width="3"/>
  </svg>
  <div class="boat-art" role="img" aria-label="Line illustration of a centre-console boat riding a wave"></div>
  <div class="wordmark"><span class="big">Dalby</span><span class="small">Marine Co</span></div>
  <div class="contact">
    <p class="name"><strong>Corwin Dalby</strong> | Dalby Marine Co</p>
    <p class="line">
      <svg viewBox="0 0 24 24" aria-hidden="true"><path d="M6.6 10.8a15 15 0 0 0 6.6 6.6l2.2-2.2a1 1 0 0 1 1-.25 11.4 11.4 0 0 0 3.6.6 1 1 0 0 1 1 1V20a1 1 0 0 1-1 1A17 17 0 0 1 3 4a1 1 0 0 1 1-1h3.5a1 1 0 0 1 1 1c0 1.25.2 2.45.6 3.6a1 1 0 0 1-.25 1z"/></svg>
      555.318.6027 |
      <svg viewBox="0 0 24 24" aria-hidden="true"><path d="M12 2a7 7 0 0 0-7 7c0 5.2 7 13 7 13s7-7.8 7-13a7 7 0 0 0-7-7zm0 9.5A2.5 2.5 0 1 1 12 6.5a2.5 2.5 0 0 1 0 5z"/></svg>
      Port Lindell, SC |
      <svg viewBox="0 0 24 24" aria-hidden="true"><path d="M3 5h18a1 1 0 0 1 1 1v12a1 1 0 0 1-1 1H3a1 1 0 0 1-1-1V6a1 1 0 0 1 1-1zm9 7 8-5H4z"/></svg>
      Corwin@dalbymarineco.example
    </p>
    <div class="rule"></div>
  </div>
  <div class="badge" role="img" aria-label="Trade association membership badge"></div>
</section>

</body>
</html>
```